Brave Roads Ahead: Holding Hope, Meeting Storms, Voicing Triumph

I want a modern and clean looking book cover. 5.25x8

Title
Brave Roads Ahead

Subtitle
Holding Hope, Meeting Storms, Voicing Triumph

I don’t just want a graphic, I want it to make sense. If it can just be the words and a textured looking background, I’ll be ok with that too. I just want it to look crisp, clean, modern.

I want the back to have my book blurb and bio attached with the pic that’s attached.

Target Market(s)

Self help

Requirements
Must have
• Modern, clean look, look professional, attract customers.

```html
<!DOCTYPE html>
<html lang="en">
<head>
<meta charset="utf-8">
<title>Brave Roads Ahead – Book Cover</title>
<link href="https://fonts.googleapis.com/css2?family=Anton&family=Oswald:wght@500;700&family=Open+Sans:wght@400;700&display=swap" rel="stylesheet">
<style>
  :root {
    --stage: #f1f1f1;
    --cover-black: #050507;
    --ink-white: #f4f4f6;
    --accent-coral: #e2544f;
    --body-grey: #d9d9dc;
    --nebula-pink: rgba(196, 64, 120, 0.55);
    --nebula-red: rgba(226, 82, 62, 0.6);
    --nebula-teal: rgba(70, 150, 140, 0.55);
  }
  * { margin: 0; padding: 0; box-sizing: border-box; }
  html, body {
    width: 1200px; height: 1000px; overflow: hidden;
    background: var(--stage);
  }
  .spread {
    position: absolute; left: 160px; top: 180px;
    display: flex; gap: 40px;
  }
  .cover {
    position: relative; width: 420px; height: 640px;
    background: var(--cover-black); overflow: hidden;
    box-shadow: 0 10px 30px rgba(0,0,0,0.25);
  }

  /* Back cover */
  .back-cover { padding: 34px 30px 30px; color: var(--body-grey);
    font-family: "Open Sans", Arial, sans-serif; font-size: 8.6px; line-height: 1.42; }
  .back-headline { font-family: "Open Sans", Arial, sans-serif; font-weight: 700;
    color: var(--accent-coral); font-size: 14px; line-height: 1.3; text-align: center;
    margin-bottom: 12px; }
  .blurb p { text-align: center; margin-bottom: 9px; }
  .bio { margin-top: 16px; }
  .bio p { margin-bottom: 0; }
  .bio strong { color: var(--ink-white); }

  /* Front cover */
  .front-cover { color: var(--ink-white); text-align: center; }
  .nebula-art {
    position: absolute; inset: 0;
    background:
      radial-gradient(ellipse 30% 40% at 28% 58%, var(--nebula-red), transparent 70%),
      radial-gradient(ellipse 35% 45% at 45% 42%, var(--nebula-pink), transparent 72%),
      radial-gradient(ellipse 40% 35% at 65% 72%, var(--nebula-teal), transparent 72%),
      var(--cover-black);
  }
  .author-name { position: relative; margin-top: 54px;
    font-family: "Oswald", Arial, sans-serif; font-weight: 700;
    font-size: 30px; color: var(--accent-coral); letter-spacing: 0.5px; }
  .book-title { position: relative; margin-top: 34px;
    font-family: "Anton", Impact, sans-serif; font-weight: 400;
    font-size: 108px; line-height: 1.06; color: rgba(244,244,246,0.92);
    text-transform: uppercase; letter-spacing: 1px; }
  .book-subtitle { position: absolute; left: 0; right: 0; bottom: 34px;
    font-family: "Oswald", Arial, sans-serif; font-weight: 500;
    font-size: 15px; color: var(--ink-white); letter-spacing: 0.3px; }
</style>
</head>
<body>
  <main class="spread">
    <section class="cover back-cover" aria-label="Back cover">
      <h2 class="back-headline">Everyone has big dreams,<br>but few give themselves the chance to live them.</h2>
      <div class="blurb">
        <p>Brave Roads Ahead: Holding Hope, Meeting Storms, Voicing Triumph is for anyone who has ever been stymied by negative self-talk, maltreatment, family problems, or has experienced anything significant that kept them from their dreams.</p>
        <p>Part memoir, part self-help book, part spiritual guide, this book offers encouragement and a helping hand to anyone who feels like their moment has passed or their time will never come.</p>
        <p>Inside, you'll find deeply personal stories and anecdotes. The author's personal experiences provide a detailed account and path to climb out of a dark spot, find your voice, dream bigger, dare to believe, and step into your purpose. If you've ever felt like where you are now is where you'll stay, or that your prayers will never be answered, this book will help you move past doubt and learn how to confidently bet on yourself.</p>
      </div>
      <div class="bio">
        <p><strong>Dana Whitfield</strong> is a helper.</p>
        <p>For as long as she can remember, she's always wanted to help others. Life circumstance, and some very tough years, set her on a path that conflicted with what was in her heart... until something shifted and she made herself and her goals a priority. A dreamer and visionary at her core, she knows all too well how much faith and courage it takes to defy expectations and carve your own path forward. Her tenacity led her in a direction that would change her life for the better. After being told she wasn't "college material" in high school, she made it her mission to never allow anyone to define who she is, and more importantly, to empower others to do the same. Today, the devout Christian, Author, Motivator, Coach, and Educational Leader, holds 3 degrees (Bachelors in Psychology, Master of Education, and Educational Specialist) and is currently in the dissertation phase of a Doctorate degree. Recently, she added Life Coach to her resume. When she's not teaching, studying, coaching, reading, listening to music, or helping others achieve their goals, she spends as much time as she can with her loving husband, their dog, her school-aged God-daughter, and countless friends.</p>
      </div>
    </section>

    <section class="cover front-cover" aria-label="Front cover">
      <div class="nebula-art" role="img" aria-label="Starry night sky with a pink, red and teal nebula and a small bird in flight"></div>
      <p class="author-name">Dana Whitfield</p>
      <h1 class="book-title">Brave<br>Roads<br>Ahead</h1>
      <p class="book-subtitle">Holding Hope, Meeting Storms, Voicing Triumph</p>
    </section>
  </main>
</body>
</html>
```